Two flyers with cover pages for business services company

We need to create two double sided A4 flyers for our company. We are a company that provides professional services for businesses in Dubai, UAE.
Please note that there are two different flyers. The design must be identical. Each has a cover page. The cover page will be duplicated for both flyers.
Please note that we have added images of the Dubai skyline, clip art as place-hold/temporary images. These can be changed to be more fitting to your design. We prefer to have free images where possible but are open to purchasing Pixelorra images if required.
We have recommended a colour palet below. You are welcome to change some colours to be more fitting to the design. However, we must have black, white and blue and per the logo.
Target Market(s)
Businesses, entrepreneurs, professionals
Industry/Entity Type
Business Service
Requirements
Must have
- The cover page should be less crowded and more visual. So mostly images with our logo and tagline.

```html
<!DOCTYPE html>
<html lang="en">
<head>
<meta charset="utf-8">
<title>Nexora – Cover</title>
<link rel="stylesheet" href="https://fonts.googleapis.com/css2?family=Titillium+Web:wght@400;600;700&display=swap">
<style>
  :root {
    --frame-black: #000000;
    --paper-white: #ffffff;
    --brand-blue: #0b74d8;
    --accent-blue: #1a9be2;
    --stripe-grey: #b8b8b8;
    --ink-dark: #333333;
  }
  * { margin: 0; padding: 0; box-sizing: border-box; }
  html, body {
    width: 931px; height: 1200px; overflow: hidden;
    background: var(--paper-white);
  }
  .cover {
    position: relative;
    width: 931px; height: 1200px;
    background: var(--paper-white);
    border: 15px solid var(--frame-black);
    overflow: hidden;
    font-family: "Titillium Web", "Segoe UI", sans-serif;
  }
  .cover__art {
    position: absolute; left: -15px; top: -15px;
    width: 931px; height: 1200px;
  }
  .brand {
    position: absolute; top: 30px; right: 30px;
    display: flex; align-items: center; gap: 14px;
  }
  .brand__dot {
    width: 46px; height: 46px; border-radius: 50%;
    background: var(--accent-blue);
  }
  .brand__name {
    font-weight: 400; font-size: 58px; line-height: 1;
    color: var(--ink-dark); letter-spacing: 0.5px;
  }
  .tagline {
    position: absolute; right: 46px; top: 180px;
    text-align: right; font-weight: 600;
    font-size: 37px; line-height: 42px; text-transform: uppercase;
  }
  .tagline__lead { display: block; color: var(--accent-blue); margin-right: 158px; }
  .tagline__follow { display: block; color: var(--ink-dark); }
  .web-address {
    position: absolute; right: 34px; bottom: 22px;
    color: var(--paper-white); font-weight: 600; font-size: 21px;
    letter-spacing: 0.5px;
  }
</style>
</head>
<body>
  <main class="cover">
    <svg class="cover__art" viewBox="0 0 931 1200" xmlns="http://www.w3.org/2000/svg">
      <defs>
        <linearGradient id="duskSky" x1="0" y1="0" x2="0" y2="1">
          <stop offset="0" stop-color="#1f2f9e"/>
          <stop offset="0.3" stop-color="#3f4cc0"/>
          <stop offset="0.55" stop-color="#7f6fc6"/>
          <stop offset="0.66" stop-color="#c98cb4"/>
          <stop offset="0.72" stop-color="#e3a0a6"/>
          <stop offset="0.78" stop-color="#4a3e68"/>
          <stop offset="0.88" stop-color="#262238"/>
          <stop offset="1" stop-color="#15131f"/>
        </linearGradient>
        <radialGradient id="cityGlow" cx="0.36" cy="0.9" r="0.45">
          <stop offset="0" stop-color="#f2c16a" stop-opacity="0.75"/>
          <stop offset="0.35" stop-color="#d9884f" stop-opacity="0.35"/>
          <stop offset="1" stop-color="#d9884f" stop-opacity="0"/>
        </radialGradient>
        <radialGradient id="horizonHaze" cx="0.12" cy="0.7" r="0.4">
          <stop offset="0" stop-color="#f0a2b8" stop-opacity="0.6"/>
          <stop offset="1" stop-color="#f0a2b8" stop-opacity="0"/>
        </radialGradient>
        <radialGradient id="upperDepth" cx="0.85" cy="0.15" r="0.55">
          <stop offset="0" stop-color="#1a2a8c" stop-opacity="0.7"/>
          <stop offset="1" stop-color="#1a2a8c" stop-opacity="0"/>
        </radialGradient>
      </defs>
      <!-- top grey stripe -->
      <polygon class="stripe-grey" fill="var(--stripe-grey)"
        points="15,318 246,228 916,390 916,400 246,246 15,328"/>
      <!-- top blue band -->
      <polygon class="band-blue" fill="var(--brand-blue)"
        points="15,328 246,246 916,400 916,410 246,268 15,336"/>
      <!-- lower black stripe -->
      <polygon class="stripe-black" fill="var(--frame-black)"
        points="15,880 246,964 916,810 916,818 246,976 15,888"/>
      <!-- lower grey wedge -->
      <polygon class="stripe-grey" fill="var(--stripe-grey)"
        points="15,868 246,934 916,800 916,810 246,964 15,880"/>
      <!-- bottom blue field -->
      <polygon class="field-blue" fill="var(--brand-blue)"
        points="15,888 246,976 916,818 916,1185 15,1185"/>
      <!-- skyline photo area -->
      <g role="img" aria-label="Photo of the Dubai city skyline at dusk with lit towers">
        <polygon fill="url(#duskSky)"
          points="15,336 246,268 916,410 916,800 246,934 15,868"/>
        <polygon fill="url(#upperDepth)"
          points="15,336 246,268 916,410 916,800 246,934 15,868"/>
        <polygon fill="url(#horizonHaze)"
          points="15,336 246,268 916,410 916,800 246,934 15,868"/>
        <polygon fill="url(#cityGlow)"
          points="15,336 246,268 916,410 916,800 246,934 15,868"/>
      </g>
    </svg>

    <div class="brand">
      <span class="brand__dot"></span>
      <span class="brand__name">Nexora</span>
    </div>

    <h1 class="tagline">
      <span class="tagline__lead">Your Business</span>
      <span class="tagline__follow">Our Connections</span>
    </h1>

    <p class="web-address">WWW.NEXORA.AE</p>
  </main>
</body>
</html>
```